Business card update

Opening a subsidiary of my company in the USA and need to update my logo.
Updates

Reason: Give more time to a good design.

I made a mistake on my briefing. It's only the business card. Thanks for alerting me on the mistake.

All the best

Leopoldo

Target Market(s)

We are an Executive Search company and our target audience are executives in large corporations.

Industry/Entity Type

Business

Requirements
Must have
• Keep the logo. In the US the company is called Declan Harrow Executive Search.

```html
<!DOCTYPE html>
<html lang="en">
<head>
<meta charset="utf-8">
<title>Declan Harrow Executive Search – Business Card</title>
<link rel="stylesheet" href="https://fonts.googleapis.com/css2?family=Open+Sans:wght@400;600&family=Roboto+Slab:wght@700&display=swap">
<style>
  :root {
    --page-bg: #e9e7e3;
    --card-top: #ffffff;
    --card-bottom: #e6e8ea;
    --ink-dark: #3b4552;
    --ink-body: #4b5560;
    --brand-teal: #2aa3ad;
    --brand-slate: #55667a;
  }
  * { margin: 0; padding: 0; box-sizing: border-box; }
  html, body {
    width: 1200px;
    height: 900px;
    overflow: hidden;
    background: var(--page-bg);
  }
  .canvas {
    position: relative;
    width: 1200px;
    height: 900px;
  }
  .business-card {
    position: absolute;
    left: 100px;
    top: 164px;
    width: 1000px;
    height: 572px;
    background: linear-gradient(180deg, var(--card-top) 0%, var(--card-top) 40%, var(--card-bottom) 100%);
    box-shadow: 0 18px 40px rgba(0, 0, 0, 0.18), 0 3px 8px rgba(0, 0, 0, 0.12);
    overflow: hidden;
  }
  .brand-lockup {
    position: absolute;
    left: 60px;
    top: 262px;
    width: 360px;
    display: flex;
    align-items: center;
    gap: 14px;
  }
  .brand-dot {
    width: 16px;
    height: 16px;
    border-radius: 50%;
    background: var(--brand-teal);
    flex: none;
  }
  .brand-name {
    font-family: 'Open Sans', sans-serif;
    font-weight: 400;
    font-size: 30px;
    letter-spacing: 0.16em;
    text-transform: uppercase;
    color: var(--brand-slate);
    white-space: nowrap;
  }
  .divider {
    position: absolute;
    left: 468px;
    top: 78px;
    width: 1.5px;
    height: 410px;
    background: var(--brand-teal);
    opacity: 0.75;
  }
  .contact-block {
    position: absolute;
    left: 506px;
    top: 70px;
    right: 30px;
  }
  .person-name {
    font-family: 'Roboto Slab', serif;
    font-weight: 700;
    font-size: 34px;
    color: var(--ink-dark);
    line-height: 1.2;
  }
  .person-title {
    font-family: 'Open Sans', sans-serif;
    font-weight: 400;
    font-size: 26px;
    color: var(--brand-teal);
    margin-top: 4px;
  }
  .address {
    font-family: 'Open Sans', sans-serif;
    font-size: 21px;
    color: var(--ink-body);
    line-height: 1.35;
    margin-top: 36px;
  }
  .contact-list {
    list-style: none;
    margin-top: 36px;
    font-family: 'Open Sans', sans-serif;
    font-size: 21px;
    color: var(--ink-body);
    line-height: 1.35;
  }
  .contact-list li {
    display: flex;
    align-items: center;
    gap: 10px;
  }
  .contact-icon {
    width: 20px;
    height: 18px;
    flex: none;
  }
</style>
</head>
<body>
<main class="canvas">
  <article class="business-card" aria-label="Business card for Declan Harrow Executive Search">
    <div class="brand-lockup">
      <span class="brand-dot"></span>
      <span class="brand-name">Declan Harrow</span>
    </div>

    <div class="divider"></div>

    <section class="contact-block">
      <h1 class="person-name">Leopoldo S. Harrow</h1>
      <p class="person-title">CEO / Founder</p>
      <p class="address">4810 Coral Bay Ave Suite 300<br>Harbor Point FL 33190</p>
      <ul class="contact-list">
        <li>
          <svg class="contact-icon" viewBox="0 0 20 18" aria-hidden="true">
            <path d="M2 6 C2 3 5 2 10 2 C15 2 18 3 18 6 L15 7 L14 5 C12 4.5 8 4.5 6 5 L5 7 Z" fill="var(--brand-teal)"/>
            <rect x="4" y="8" width="12" height="8" rx="1.5" fill="var(--brand-teal)"/>
            <circle cx="10" cy="12" r="2" fill="#fff"/>
          </svg>
          <span>305 555 0148</span>
        </li>
        <li>
          <svg class="contact-icon" viewBox="0 0 20 18" aria-hidden="true">
            <rect x="1.5" y="3" width="17" height="12" fill="none" stroke="var(--brand-teal)" stroke-width="2"/>
            <path d="M2 4 L10 10 L18 4" fill="none" stroke="var(--brand-teal)" stroke-width="2"/>
          </svg>
          <span>lharrow@dhexecsearch.com</span>
        </li>
        <li>
          <svg class="contact-icon" viewBox="0 0 20 18" aria-hidden="true">
            <circle cx="10" cy="9" r="7.5" fill="var(--brand-teal)"/>
            <path d="M2.5 9 H17.5 M10 1.5 C6.5 5 6.5 13 10 16.5 M10 1.5 C13.5 5 13.5 13 10 16.5" fill="none" stroke="#fff" stroke-width="1.2"/>
          </svg>
          <span>www.dhexecsearch.com</span>
        </li>
      </ul>
    </section>
  </article>
</main>
</body>
</html>
```